Fast-casual chicken restaurant Plume Rally needs a catering menu design

We need a catering menu designed for Plume Rally. We are looking to design a 24x36in landscape menu board for our new catering menu. The catering memo attached includes our catering menu and Plume Rally branding. More information about our brand can be found at https://plumerally.example/.

```html
<!DOCTYPE html>
<html lang="en">
<head>
<meta charset="utf-8">
<title>Plume Rally — Catering Menu</title>
<link href="https://fonts.googleapis.com/css2?family=Montserrat:wght@600;700;800&display=swap" rel="stylesheet">
<style>
  :root{
    --red:#d0342b;
    --label-red:#cf2f28;
    --yellow:#fcd237;
    --cream:#fbf3e4;
    --ink:#1b1b1b;
    --white:#ffffff;
    --photo-warm:#e8c98f;
    --photo-deep:#b5642c;
  }
  *{margin:0;padding:0;box-sizing:border-box}
  html,body{width:1200px;height:800px;overflow:hidden;background:var(--cream)}
  body{font-family:"Montserrat",Arial,sans-serif;color:var(--ink)}
  .menu-board{position:relative;width:1200px;height:800px;overflow:hidden;background:var(--cream)}
  .backdrop-food{position:absolute;left:140px;top:0;width:880px;height:510px;
    background:radial-gradient(ellipse at 55% 45%,rgba(232,201,143,.55),rgba(251,243,228,0) 70%);}
  .side-photo{position:absolute;left:1018px;top:0;width:182px;height:510px;border-radius:70px 0 0 0;
    background:linear-gradient(160deg,#c9a678 0%,#e9dcc6 30%,var(--photo-deep) 60%,#8c3a1c 80%,#d8b884 100%);}
  .bottom-band{position:absolute;left:0;top:510px;width:1200px;height:290px;background:var(--yellow)}
  section{position:absolute;inset:0}
  .ribbon{position:absolute;background:var(--red);color:var(--white);font-weight:700;
    display:flex;align-items:center;letter-spacing:.5px;font-size:21px}
  .ribbon--tail{clip-path:polygon(0 0,100% 0,92% 50%,100% 100%,0 100%);padding-left:32px;height:39px}
  .ribbon--point{clip-path:polygon(7% 0,93% 0,100% 50%,93% 100%,7% 100%,0 50%);justify-content:center;height:34px}
  .t{position:absolute;white-space:nowrap;font-weight:700;font-size:20px;line-height:24px}
  .head{color:var(--label-red)}
  .cat-label{color:var(--label-red);text-align:center;width:134px}
  .cat-text{font-size:18.5px}
</style>
</head>
<body>
<main class="menu-board">
  <div class="backdrop-food" role="img" aria-label="Faded photo of a platter of crispy chicken wings"></div>
  <div class="side-photo" role="img" aria-label="Photo of a table spread with chicken tenders, wings, waffle fries and dipping sauces"></div>
  <div class="bottom-band"></div>

  <section class="packaged-deals">
    <div class="ribbon ribbon--tail" style="left:0;top:19px;width:306px">PACKAGED DEALS</div>
    <span class="t head" style="left:26px;top:74px">NAME</span>
    <span class="t head" style="left:196px;top:74px">FEEDS</span>
    <span class="t head" style="left:525px;top:74px">ITEMS</span>
    <span class="t head" style="left:940px;top:74px">PRICE</span>

    <span class="t" style="left:27px;top:114px">FAMILY</span>
    <span class="t" style="left:223px;top:114px">4</span>
    <span class="t" style="left:328px;top:114px">12 tenders, sauces, dressing, large side, 2L</span>
    <span class="t" style="left:942px;top:112px">$24.99</span>

    <span class="t" style="left:27px;top:151px">TAILGATE</span>
    <span class="t" style="left:219px;top:151px">10</span>
    <span class="t" style="left:328px;top:151px">20 tenders, 30 wings, sauces, dressing, 1 party side</span>
    <span class="t" style="left:942px;top:149px">$75.99</span>

    <span class="t" style="left:30px;top:188px">HOUSE PARTY</span>
    <span class="t" style="left:219px;top:188px">10</span>
    <span class="t" style="left:328px;top:188px">20 tenders, 60 wings, sauces, 2 party sides,</span>
    <span class="t" style="left:328px;top:212px">2 party salads, dressings, 2 2L</span>
    <span class="t" style="left:942px;top:188px">$155.99</span>
  </section>

  <section class="per-person-deals">
    <div class="ribbon ribbon--tail" style="left:0;top:246px;width:320px">PER PERSON DEALS</div>
    <span class="t head" style="left:33px;top:301px">NAME</span>
    <span class="t head" style="left:200px;top:299px">FEEDS</span>
    <span class="t head" style="left:532px;top:298px">ITEMS</span>
    <span class="t head" style="left:945px;top:293px">PRICE</span>

    <span class="t" style="left:34px;top:346px">SNACK</span>
    <span class="t" style="left:236px;top:342px">1</span>
    <span class="t" style="left:328px;top:341px">2 tenders, sauce, dressing, 1 reg side</span>
    <span class="t" style="left:946px;top:340px">$7.00</span>

    <span class="t" style="left:34px;top:383px">PARTY</span>
    <span class="t" style="left:236px;top:383px">1</span>
    <span class="t" style="left:328px;top:378px">2 tenders, 3 wings, sauce, dressing, 1 reg side,</span>
    <span class="t" style="left:328px;top:402px">12oz/fountain drink</span>
    <span class="t" style="left:946px;top:374px">$11.00</span>

    <span class="t" style="left:34px;top:439px">FEAST</span>
    <span class="t" style="left:236px;top:439px">1</span>
    <span class="t" style="left:328px;top:437px">2 tenders, 6 wings, sauce, dressing, 1 reg side,</span>
    <span class="t" style="left:328px;top:461px">dessert, 20 oz drink</span>
    <span class="t" style="left:946px;top:439px">$15.00</span>
  </section>

  <section class="a-la-carte">
    <div class="ribbon ribbon--point" style="left:112px;top:501px;width:302px">A LA CARTE</div>
    <span class="t head" style="left:29px;top:547px">ITEMS</span>
    <span class="t head" style="left:266px;top:547px">INCREMENTS</span>
    <span class="t head" style="left:455px;top:547px">PRICE</span>

    <span class="t" style="left:29px;top:583px">Wings</span><span class="t" style="left:284px;top:583px">50, 75, 100</span><span class="t" style="left:460px;top:583px">$xx.xx</span>
    <span class="t" style="left:29px;top:607px">Tenders</span><span class="t" style="left:284px;top:607px">30, 45, 60</span><span class="t" style="left:460px;top:607px">$xx.xx</span>
    <span class="t" style="left:29px;top:631px">Waffle Fries</span><span class="t" style="left:284px;top:631px">Party Size</span><span class="t" style="left:460px;top:631px">$13.99</span>
    <span class="t" style="left:29px;top:655px">Garlic Parm Tots</span><span class="t" style="left:284px;top:655px">Party Size</span><span class="t" style="left:460px;top:655px">$13.99</span>
    <span class="t" style="left:29px;top:679px">Chicken Caesar Salad</span><span class="t" style="left:284px;top:679px">Party Size</span><span class="t" style="left:460px;top:679px">$38.99</span>
    <span class="t" style="left:29px;top:703px">Caesar Salad</span><span class="t" style="left:284px;top:703px">Party Size</span><span class="t" style="left:460px;top:703px">$27.99</span>
    <span class="t" style="left:29px;top:727px">Any Sauce</span><span class="t" style="left:284px;top:727px">8 oz</span><span class="t" style="left:466px;top:727px">$1.99</span>
    <span class="t" style="left:29px;top:751px">Cheese Sauce</span><span class="t" style="left:284px;top:751px">8 oz</span><span class="t" style="left:466px;top:751px">$2.49</span>
  </section>

  <section class="catering-menu">
    <div class="ribbon ribbon--point" style="left:734px;top:501px;width:300px">CATERING MENU</div>
    <span class="t cat-label" style="left:550px;top:547px">FLAVORS</span>
    <span class="t cat-text" style="left:694px;top:547px">Honey Mustard, Hot Lemon Pepper,</span>
    <span class="t cat-text" style="left:694px;top:568px">Jamaican Jerk, Mango Habanero, Sweet Chili</span>

    <span class="t cat-label" style="left:550px;top:604px">BBQ</span>
    <span class="t cat-text" style="left:694px;top:598px">Cajun BBQ, Citrus Chipotle, Golden BBBQ,</span>
    <span class="t cat-text" style="left:694px;top:620px">Honey BBQ, Kickin BBQ</span>

    <span class="t cat-label" style="left:550px;top:661px">DRY RUBS</span>
    <span class="t cat-text" style="left:694px;top:652px">7 Pepper, Cajun, Garlic Parm, Lemon Pepper,</span>
    <span class="t cat-text" style="left:694px;top:674px">West Texas Mesquite</span>

    <span class="t cat-label" style="left:550px;top:706px">TERIYAKI</span>
    <span class="t cat-text" style="left:694px;top:706px">Cajun Teriyaki, Spicy Teriyaki, Traditional Teriyaki</span>

    <span class="t cat-label" style="left:550px;top:744px">BUFFALO</span>
    <span class="t cat-text" style="left:694px;top:740px">Mild, Classic Heat, Red Hot, Extra Hot,</span>
    <span class="t cat-text" style="left:694px;top:762px">Inferno</span>
  </section>
</main>
</body>
</html>
```